Design a website banner for Squarespace website

I need someone to take the image file and turn it into a banner for our website. I would also like the colours changed in our logo to match the colours of the banner.
- I will need a high resolution copy of the 2 logo designs with changed colours
- I need the colour number codes for each colour so that I can match the colours in the website accordingly.
I would like a banner without the logo and a few design variations that can be used on other pages so that the banner can vary for each page.
- Each banner will need to have white space for some basic text.

Sick

```html
<!DOCTYPE html>
<html lang="en">
<head>
<meta charset="utf-8">
<title>Website Banners – Feel Better / Achieve More</title>
<link rel="stylesheet" href="https://fonts.googleapis.com/css2?family=Nunito:wght@500;700;800&display=swap">
<style>
  :root {
    --backdrop: #5f6062;
    --navy: #0d2d6e;
    --navy-deep: #0e1f52;
    --orange: #e8610e;
    --yellow: #fff200;
    --white: #ffffff;
    --banner-blue: #1f3566;
  }
  html, body {
    margin: 0;
    padding: 0;
    width: 1200px;
    height: 1000px;
    overflow: hidden;
    background: var(--backdrop);
    font-family: "Nunito", Arial, sans-serif;
  }
  .canvas {
    position: relative;
    width: 1200px;
    height: 1000px;
  }
  .banner {
    position: absolute;
    left: 120px;
    width: 963px;
    height: 315px;
    display: block;
  }
  .banner--feel { top: 101px; }
  .banner--achieve { top: 543px; }
  .headline { font-family: "Nunito", Arial, sans-serif; }
  .headline--feel { fill: var(--navy); font-weight: 800; font-size: 122px; letter-spacing: -2px; }
  .headline--better { fill: var(--orange); font-weight: 500; font-size: 100px; letter-spacing: -1px; }
  .headline--achieve { fill: var(--yellow); font-weight: 800; font-size: 84px; letter-spacing: -1px; }
  .brand-name { font-family: "Nunito", Arial, sans-serif; font-weight: 700; }
  .brand-name--light { fill: var(--white); font-size: 22px; }
  .brand-name--yellow { fill: var(--yellow); font-size: 26px; }
</style>
</head>
<body>
<main class="canvas">

  <!-- Banner one: Feel Better -->
  <svg class="banner banner--feel" viewBox="0 0 963 315" xmlns="http://www.w3.org/2000/svg">
    <defs>
      <linearGradient id="sunlit-summit" x1="0" y1="0" x2="1" y2="0">
        <stop offset="0" stop-color="#9c7748"/>
        <stop offset="0.25" stop-color="#c2a074"/>
        <stop offset="0.45" stop-color="#eadcc6"/>
        <stop offset="0.65" stop-color="#ffffff" stop-opacity="0"/>
      </linearGradient>
      <radialGradient id="mosaic-glow-top" cx="0.8" cy="0.2" r="0.7">
        <stop offset="0" stop-color="#f7b52a" stop-opacity="0.45"/>
        <stop offset="0.5" stop-color="#1e8fd0" stop-opacity="0.2"/>
        <stop offset="1" stop-color="#1e8fd0" stop-opacity="0"/>
      </radialGradient>
      <radialGradient id="mosaic-glow-bottom" cx="0.3" cy="0.8" r="0.7">
        <stop offset="0" stop-color="#e63b3f" stop-opacity="0.4"/>
        <stop offset="0.5" stop-color="#13a08a" stop-opacity="0.2"/>
        <stop offset="1" stop-color="#13a08a" stop-opacity="0"/>
      </radialGradient>
    </defs>
    <rect class="banner__base" width="963" height="315" fill="var(--white)"/>
    <rect class="banner__photo" x="0" y="0" width="963" height="315" fill="url(#sunlit-summit)"
          role="img" aria-label="Photo: man sitting on a sunlit mountain rock with arms spread wide"/>
    <circle class="banner__space-outline" cx="880" cy="150" r="240" fill="none"
            stroke="#c9cbd2" stroke-width="2" stroke-dasharray="2 5"/>
    <rect class="banner__mosaic" x="650" y="0" width="313" height="190" fill="url(#mosaic-glow-top)"
          role="img" aria-label="Multicolour diamond mosaic"/>
    <rect class="banner__mosaic" x="0" y="130" width="220" height="185" fill="url(#mosaic-glow-bottom)"
          role="img" aria-label="Multicolour diamond mosaic"/>
    <circle class="banner__brand-arc-dots" cx="880" cy="600" r="410" fill="none"
            stroke="var(--navy-deep)" stroke-width="3" stroke-dasharray="2 5"/>
    <circle class="banner__brand-arc" cx="880" cy="600" r="398" fill="var(--navy-deep)"/>
    <text class="headline headline--feel" x="333" y="145">Feel</text>
    <text class="headline headline--better" x="376" y="228">Better</text>
    <rect class="brand-mark" x="690" y="257" width="14" height="14" fill="var(--white)"/>
    <text class="brand-name brand-name--light" x="712" y="271">Brightpath Wellbeing</text>
  </svg>

  <!-- Banner two: Achieve More -->
  <svg class="banner banner--achieve" viewBox="0 0 963 315" xmlns="http://www.w3.org/2000/svg">
    <defs>
      <linearGradient id="mountain-sky" x1="0" y1="0" x2="1" y2="0">
        <stop offset="0" stop-color="#8fb0d8"/>
        <stop offset="0.3" stop-color="#4d6fa6"/>
        <stop offset="0.6" stop-color="#2a427a"/>
        <stop offset="1" stop-color="var(--banner-blue)"/>
      </linearGradient>
      <radialGradient id="mosaic-glow-top-2" cx="0.8" cy="0.2" r="0.7">
        <stop offset="0" stop-color="#f7b52a" stop-opacity="0.35"/>
        <stop offset="0.5" stop-color="#e63b3f" stop-opacity="0.15"/>
        <stop offset="1" stop-color="#e63b3f" stop-opacity="0"/>
      </radialGradient>
      <radialGradient id="mosaic-glow-bottom-2" cx="0.3" cy="0.8" r="0.7">
        <stop offset="0" stop-color="#e63b3f" stop-opacity="0.35"/>
        <stop offset="0.5" stop-color="#13a08a" stop-opacity="0.15"/>
        <stop offset="1" stop-color="#13a08a" stop-opacity="0"/>
      </radialGradient>
    </defs>
    <rect class="banner__photo" width="963" height="315" fill="url(#mountain-sky)"
          role="img" aria-label="Photo: hiker in a red jacket cheering on a snowy mountain ridge"/>
    <rect class="banner__mosaic" x="650" y="0" width="313" height="190" fill="url(#mosaic-glow-top-2)"
          role="img" aria-label="Multicolour diamond mosaic"/>
    <rect class="banner__mosaic" x="0" y="130" width="220" height="185" fill="url(#mosaic-glow-bottom-2)"
          role="img" aria-label="Multicolour diamond mosaic"/>
    <circle class="banner__space-dots" cx="473" cy="376" r="232" fill="none"
            stroke="var(--yellow)" stroke-width="3" stroke-dasharray="2 5"/>
    <circle class="banner__text-space" cx="473" cy="376" r="219" fill="var(--white)"/>
    <text class="headline headline--achieve" x="228" y="132">Achieve More</text>
    <rect class="brand-mark" x="714" y="204" width="18" height="18" fill="var(--yellow)"/>
    <text class="brand-name brand-name--yellow" x="742" y="222">Brightpath</text>
    <text class="brand-name brand-name--yellow" x="742" y="252">Wellbeing</text>
  </svg>

</main>
</body>
</html>
```